Business card alterations

I have changed my business name from Orvan Laser Rejuvenation Clinic to simply "Orvan Laser Clinic' and need this logo changed to reflect same

Orvan Laser Clinic
Est. 2004

I also need new business cards with above logo included and this attached card changed to the following.
Marguerite Halcombe
Dermal Aesthetician
Grad Cert in Laser & IPL Treatments

I need at least one logo in less than 4mb so I can upload into my newsletter format so I can upload to newsletters, emails etc

Thanks
Marg

Industry/Entity Type

Business

```html
<!DOCTYPE html>
<html lang="en">
<head>
<meta charset="utf-8">
<title>Orvan Laser Clinic – Business Card</title>
<link rel="stylesheet" href="https://fonts.googleapis.com/css2?family=Open+Sans:wght@400;600;700&display=swap">
<style>
  :root {
    --backdrop: #e9e6e1;
    --card-green: #00a05a;
    --card-ink: #ffffff;
    --card-shadow: rgba(0, 0, 0, 0.18);
  }
  * { margin: 0; padding: 0; box-sizing: border-box; }
  html, body {
    width: 1200px;
    height: 870px;
    overflow: hidden;
    background: var(--backdrop);
  }
  .canvas {
    width: 1200px;
    height: 870px;
    display: flex;
    align-items: center;
    justify-content: center;
  }
  .business-card {
    width: 478px;
    height: 782px;
    background: var(--card-green);
    color: var(--card-ink);
    font-family: "Open Sans", Arial, sans-serif;
    box-shadow: 0 10px 30px var(--card-shadow);
    display: flex;
    flex-direction: column;
    align-items: center;
    text-align: center;
    padding: 84px 36px 64px;
  }
  .brand-name {
    font-size: 76px;
    font-weight: 600;
    line-height: 1;
  }
  .clinic-name {
    margin-top: 42px;
    font-size: 25px;
    font-weight: 600;
    letter-spacing: 5px;
  }
  .clinic-established {
    margin-top: 2px;
    font-size: 19px;
    font-weight: 600;
    letter-spacing: 4px;
  }
  .qualification {
    margin-top: 30px;
    font-size: 19px;
    font-weight: 400;
    letter-spacing: 0.3px;
  }
  .practitioner {
    margin-top: 70px;
  }
  .practitioner__name {
    font-size: 24px;
    font-weight: 700;
  }
  .practitioner__role {
    margin-top: 2px;
    font-size: 16px;
    font-weight: 400;
  }
  .contact {
    margin-top: auto;
    list-style: none;
    font-size: 19px;
    line-height: 1.45;
    font-weight: 400;
  }
  .contact__phone { font-weight: 700; }
</style>
</head>
<body>
  <main class="canvas">
    <article class="business-card">
      <p class="brand-name">Orvan</p>
      <p class="clinic-name">Orvan Laser Clinic</p>
      <p class="clinic-established">Est. 2004</p>
      <p class="qualification">Grad Cert in Laser &amp; IPL Treatments</p>
      <div class="practitioner">
        <p class="practitioner__name">Marguerite Halcombe</p>
        <p class="practitioner__role">Dermal Aesthetician</p>
      </div>
      <ul class="contact">
        <li class="contact__phone">(08) 7410 2255</li>
        <li>info@orvan.com.au</li>
        <li>www.orvan.com.au</li>
        <li>48 Fernleigh Avenue Marbury SA 5071</li>
      </ul>
    </article>
  </main>
</body>
</html>
```